Financial Coaching & Personal Development

I’m desiring a classic business card for my financial coaching and personal development business. The colors I have started with are a goldish brown and hunter green. The brownish color represents soil and green represents growth. I don’t want it it to look masculine. I want the brown to be more of a golden color. I want the color combination and overall design to be timeless not trendy. The logo can be changed as long as it represents growth- moving from where you are to where you want to be.

Target Market(s)

Working Adults with median income $65k; small businesses with a minimum of 20 employees

Industry/Entity Type

Consulting

Contact Information for Business Card

Marla Pettit, MBA
Certified Financial Coach

Font styles to use
Serif

Requirements
Must have
• Logo
My name
Business description
Email marla.pettit@brightwaycoachhub
Phone number 555-314-7829
Nice to have
• Slogan

```html
<!DOCTYPE html>
<html lang="en">
<head>
<meta charset="utf-8">
<title>Brightway Coach Hub – Business Card</title>
<link href="https://fonts.googleapis.com/css2?family=Playfair+Display:ital,wght@0,400;0,700;1,400&display=swap" rel="stylesheet">
<style>
  :root {
    --gold: #7b5a26;
    --gold-deep: #6e5222;
    --green: #2e8b45;
    --green-bright: #2f9a4a;
    --paper: #ffffff;
    --backdrop: #2a2a2a;
    --ink-light: #ffffff;
  }
  * { box-sizing: border-box; margin: 0; padding: 0; }
  html, body {
    width: 1200px; height: 900px; overflow: hidden;
    background: var(--backdrop);
    font-family: "Playfair Display", Georgia, serif;
  }
  .canvas {
    position: relative; width: 1200px; height: 900px;
  }
  .card {
    position: absolute; left: 250px; width: 700px; height: 400px;
    box-shadow: 0 10px 30px rgba(0,0,0,.45);
  }
  .card--front { top: 35px; background: var(--paper); }
  .card--back {
    top: 465px;
    background: linear-gradient(125deg, var(--gold) 0%, var(--gold-deep) 30%, #5c7a34 65%, var(--green-bright) 100%);
    display: flex; flex-direction: column; align-items: center; justify-content: center;
    color: var(--ink-light);
  }

  .brand {
    display: flex; align-items: center; justify-content: center; gap: 14px;
  }
  .brand__dot {
    width: 26px; height: 26px; border-radius: 50%; background: var(--green);
  }
  .brand__name {
    font-weight: 700; font-size: 34px; letter-spacing: 2px; text-transform: uppercase;
    color: var(--gold);
  }
  .tagline {
    font-size: 16px; color: var(--green); text-align: center; margin-top: 8px;
  }

  .card--front .brand-block { position: absolute; top: 100px; left: 0; right: 0; }

  .person { position: absolute; top: 238px; left: 0; right: 0; }
  .person__row { display: flex; align-items: center; }
  .person__rule { flex: 1; height: 1.5px; background: var(--gold); }
  .person__name {
    padding: 0 18px; font-size: 28px; font-weight: 700; color: var(--gold);
  }
  .person__title {
    text-align: center; font-size: 16px; color: var(--green); margin-top: 2px;
  }
  .contact {
    text-align: center; font-size: 14px; color: var(--gold); margin-top: 18px;
  }

  .card--back .brand__dot { background: var(--ink-light); }
  .card--back .brand__name { color: var(--ink-light); }
  .card--back .tagline { color: var(--ink-light); }
</style>
</head>
<body>
<main class="canvas">
  <section class="card card--front" aria-label="Business card front">
    <div class="brand-block">
      <div class="brand">
        <span class="brand__dot" aria-hidden="true"></span>
        <span class="brand__name">Brightway Coach Hub</span>
      </div>
      <p class="tagline">Financial Education &amp; Personal Development</p>
    </div>
    <div class="person">
      <div class="person__row">
        <span class="person__rule"></span>
        <h1 class="person__name">Marla Pettit, MBA</h1>
        <span class="person__rule"></span>
      </div>
      <p class="person__title">Certified Financial Coach</p>
      <p class="contact">P : 555-314-7829 / E : marla.pettit@brightwaycoachhub</p>
    </div>
  </section>

  <section class="card card--back" aria-label="Business card back">
    <div class="brand">
      <span class="brand__dot" aria-hidden="true"></span>
      <span class="brand__name">Brightway Coach Hub</span>
    </div>
    <p class="tagline">Financial Education &amp; Personal Development</p>
  </section>
</main>
</body>
</html>
```